What makes us Different Managed Communications Services Provider Flyer

We need a flyer to explain why we are different than other "managed IT services" company. Gives a brief description of our company and services that can entice clients and potential clients to setup a FREE consultation with us. This will become part of an ongoing marketing campaign that includes emails, leave behinds, brochures, and more

```html
<!DOCTYPE html>
<html lang="en">
<head>
<meta charset="utf-8">
<title>Northbeam Voice &amp; Data – More Than Just a Managed IT Provider</title>
<link rel="stylesheet" href="https://fonts.googleapis.com/css2?family=Orbitron:wght@800&family=Outfit:wght@300;400;500;600;700;800&display=swap">
<style>
  :root{
    --navy:#0b2a5c;
    --deep-blue:#0a4aa6;
    --royal:#0d57b8;
    --cyan:#05d3ea;
    --sky:#1b8fd6;
    --ink:#0c0c0c;
    --body:#4e4e52;
    --white:#ffffff;
    --paper:#f7f8fa;
  }
  *{margin:0;padding:0;box-sizing:border-box}
  html,body{width:927px;height:1200px;overflow:hidden;background:var(--paper)}
  .flyer{position:relative;width:927px;height:1200px;overflow:hidden;background:var(--paper);font-family:"Outfit",sans-serif;color:var(--body)}
  .hero-shapes{position:absolute;left:0;top:0;width:927px;height:560px}
  .cta-pill{position:absolute;left:243px;top:77px;width:441px;height:46px;border-radius:23px;
    background:linear-gradient(180deg,#2fa8ee 0%,#0b62c4 100%);border:1.5px solid rgba(255,255,255,.75);
    color:var(--white);font-weight:700;font-size:15.5px;letter-spacing:-.1px;display:flex;align-items:center;justify-content:center}
  .hero-title{position:absolute;left:0;top:138px;width:927px;text-align:center;font-family:"Orbitron",sans-serif;font-weight:800;
    color:var(--white);font-size:35px;line-height:46px;letter-spacing:0}
  .hero-subtitle{position:absolute;left:0;top:237px;width:927px;text-align:center;color:var(--white);font-weight:500;font-size:23px;letter-spacing:.2px}
  .brand-hex{position:absolute;left:143px;top:323px;width:191px;height:191px}
  .brand-name{position:absolute;left:143px;top:430px;width:191px;text-align:center;font-weight:700;font-size:15px;color:var(--ink)}
  .brand-dot{display:inline-block;width:10px;height:10px;border-radius:50%;background:var(--royal);margin-right:6px;vertical-align:0}
  .headline{position:absolute;right:60px;top:410px;text-align:right;font-weight:800;font-size:34px;line-height:45px;color:var(--ink);letter-spacing:-.3px}
  .copy{position:absolute;font-size:11.2px;line-height:23.2px;text-align:justify;color:var(--body)}
  .copy p+p{margin-top:9.5px}
  .intro{left:59px;top:529px;width:379px}
  .clients-copy{left:476px;top:508px;width:392px}
  .rule{position:absolute;left:0;top:762px;width:375px;height:2px;background:var(--deep-blue)}
  .section-title{position:absolute;left:59px;top:776px;font-weight:800;font-size:18.5px;color:var(--sky);letter-spacing:-.2px}
  .commitment-copy{left:59px;top:805px;width:379px}
  .legacy-pill{position:absolute;left:478px;top:744px;width:389px;height:43px;border-radius:22px;background:var(--deep-blue);
    color:var(--white);font-weight:800;font-size:19px;display:flex;align-items:center;justify-content:center;letter-spacing:-.2px}
  .legacy-copy{left:476px;top:800px;width:392px}
  .legacy-copy .callout{color:var(--deep-blue);font-weight:500;margin-top:7px}
  .approach{position:absolute;left:59px;top:1006px;width:810px;height:177px;border-radius:22px;
    background:linear-gradient(180deg,#05d6ec 0%,#0a9fd8 45%,#0a4aa6 100%);color:var(--white)}
  .approach-title{position:absolute;left:25px;top:24px;font-weight:700;font-size:22.5px;line-height:30px;letter-spacing:-.3px}
  .approach-text{position:absolute;left:25px;top:87px;width:300px;font-size:11px;line-height:20.7px}
  .approach-divider{position:absolute;left:348px;top:15px;width:1px;height:148px;background:rgba(255,255,255,.35)}
  .benefit{position:absolute;font-size:12px;line-height:20.7px;padding-left:20px}
  .benefit svg{position:absolute;left:0;top:4px;width:12px;height:12px}
  .b1{left:374px;top:20px;width:190px}
  .b2{left:374px;top:93px;width:190px}
  .b3{left:584px;top:20px;width:215px}
  .b4{left:584px;top:71px;width:215px}
  .page-code{position:absolute;left:895px;top:1173px;font-weight:700;font-size:9px;color:var(--ink)}
</style>
</head>
<body>
<main class="flyer">
  <svg class="hero-shapes" viewBox="0 0 927 560">
    <defs>
      <linearGradient id="heroTone" x1="0" y1="0" x2="1" y2="1">
        <stop offset="0" stop-color="#0a2a5e"/>
        <stop offset=".45" stop-color="#0c3f86"/>
        <stop offset="1" stop-color="#3a5f8f"/>
      </linearGradient>
      <linearGradient id="cornerTone" x1="0" y1="0" x2="1" y2="1">
        <stop offset="0" stop-color="#06d3ea"/>
        <stop offset="1" stop-color="#0a4aa6"/>
      </linearGradient>
    </defs>
    <polygon role="img" aria-label="Photo of a hand using a tablet in front of glowing cloud and data icons" points="0,0 927,0 927,313 708,357 334,428 0,316" fill="url(#heroTone)"/>
    <polygon points="0,330 143,396 0,555" fill="#05d3ea"/>
    <polygon points="708,357 927,313 927,475" fill="url(#cornerTone)"/>
  </svg>

  <div class="cta-pill">SCHEDULE YOUR FREE CONSULTATION TODAY!</div>
  <h1 class="hero-title">MORE THAN JUST A<br>MANAGED IT PROVIDER</h1>
  <p class="hero-subtitle">OUR LEGACY OF EXCELLENCE</p>

  <svg class="brand-hex" viewBox="0 0 191 191" aria-hidden="true">
    <polygon points="95.5,0 191,52 191,139 95.5,191 0,139 0,52" fill="#ffffff"/>
  </svg>
  <div class="brand-name"><span class="brand-dot"></span>Northbeam Voice &amp; Data</div>

  <h2 class="headline">OUR CLIENTS STAY<br>BECAUSE WE DELIVER</h2>

  <div class="copy clients-copy">
    <p>For over 40 years, we have maintained a standard of excellence that other companies simply cannot compare with. Our team of experts consistently goes above and beyond, ensuring that clients not only get the support they need but also receive the strategic guidance necessary to stay ahead in an ever-evolving digital landscape.</p>
    <p>Our 90-day performance review process ensures that we continuously improve our service based on client feedback. This process allows us to adapt, refine, and enhance our approach, providing a truly personalized IT experience that aligns with business objectives.</p>
  </div>

  <div class="copy intro">
    <p>At our company, we are far more than your typical managed IT provider. Since our founding in 1983, we have built a reputation based on trust, reliability, and unparalleled service. With client relationships spanning 20 to 30 years, we have demonstrated a level of commitment that few IT firms can match. What sets us apart is not just our technical expertise but the deep, long-term partnerships we cultivate with our clients—many of whom have stayed with us without ever being locked into a contract. That is a testament to the exceptional quality of our service and the trust we have earned over decades.</p>
  </div>

  <div class="rule"></div>
  <h3 class="section-title">A COMMITMENT BEYOND CONTRACTS</h3>
  <div class="copy commitment-copy">
    <p>Unlike many managed IT providers who rely on rigid contracts to retain clients, we believe that service excellence speaks for itself. The longevity of our client relationships is rooted in our ability to anticipate needs, resolve challenges before they escalate, and proactively enhance network &amp; communication infrastructures. Our comprehensive checklists, questionnaires, policies, and procedures, attention to details ensure that every client receives a tailored, best-in-class experience from day one.</p>
  </div>

  <h3 class="legacy-pill">A LEGACY OF TRUST &amp; RELIABILITY</h3>
  <div class="copy legacy-copy">
    <p>The fact that many of our clients have remained with us for decades without a formal contract speaks volumes about the trust we have built. We don’t lock in clients with paperwork—we keep them with results. That’s the difference between a standard managed IT provider and an IT partner who genuinely cares.</p>
    <p class="callout">If you’re looking for an IT provider that will treat your business as if it were their own, look no further. Our legacy of service, innovation, and commitment to our clients is what sets us apart from the rest.</p>
  </div>

  <section class="approach">
    <h3 class="approach-title">A HOLISTIC APPROACH TO IT<br>MANAGEMENT</h3>
    <p class="approach-text">We don’t just manage IT—we integrate ourselves into your business, ensuring that technology aligns with your strategic goals.</p>
    <div class="approach-divider"></div>
    <div class="benefit b1"><svg viewBox="0 0 12 12"><rect x="1" y="1.5" width="9" height="9" rx="1.5" fill="none" stroke="#fff" stroke-width="1.3"/><path d="M3.3 6l2 2 5.2-6" fill="none" stroke="#fff" stroke-width="1.5"/></svg>Proactive cybersecurity assessments that help keep businesses secure.</div>
    <div class="benefit b2"><svg viewBox="0 0 12 12"><rect x="1" y="1.5" width="9" height="9" rx="1.5" fill="none" stroke="#fff" stroke-width="1.3"/><path d="M3.3 6l2 2 5.2-6" fill="none" stroke="#fff" stroke-width="1.5"/></svg>Comprehensive backup and disaster recovery solutions that provide peace of mind.</div>
    <div class="benefit b3"><svg viewBox="0 0 12 12"><rect x="1" y="1.5" width="9" height="9" rx="1.5" fill="none" stroke="#fff" stroke-width="1.3"/><path d="M3.3 6l2 2 5.2-6" fill="none" stroke="#fff" stroke-width="1.5"/></svg>Strategic IT Roadmaps customized to drive business growth.</div>
    <div class="benefit b4"><svg viewBox="0 0 12 12"><rect x="1" y="1.5" width="9" height="9" rx="1.5" fill="none" stroke="#fff" stroke-width="1.3"/><path d="M3.3 6l2 2 5.2-6" fill="none" stroke="#fff" stroke-width="1.5"/></svg>Industry-leading response times and dedicated support teams focused on delivering an exceptional client experience.</div>
  </section>

  <span class="page-code">C58</span>
</main>
</body>
</html>
```